Sports Management Agency Website Design

Need a website design for a sports management agency with services as outlined in attached document.

Will need links to social media, section for partners, and ability for member/partner login.

Branding already established refer to attached files.

Look and feel professional consulting/agency, not too sporty.

Similar competitor businesses are all other sports agents.

Hi, Thanks for the efforts so far. Please don't use too much orange on the site, it is great in the logo, but would prefer darker colours that contrast with the Orange. Cheers Pieter

Industry/Entity Type

Media

Number of Pages Required

1 page

Font styles to use
Sans Serif

Requirements
Must have
• See above and brief file....reference existing logo attached.

```html
<!DOCTYPE html>
<html lang="en">
<head>
<meta charset="utf-8">
<title>Kestrel Sports Management</title>
<link href="https://fonts.googleapis.com/css2?family=Abel&family=Jost:wght@600;700&family=Open+Sans:wght@400;600&family=Roboto+Condensed:wght@300;400&display=swap" rel="stylesheet">
<style>
  :root {
    --red: #f23535;
    --orange: #f05a2a;
    --navy: #1b1f7a;
    --ink: #2b2b2b;
    --dark: #1f1f1f;
    --panel: #1e1e1e;
    --paper: #f6f6f6;
    --rule: #f5c3c3;
    --white: #ffffff;
    --hero-top: #6d7570;
    --hero-bottom: #5f7d2c;
  }
  * { margin: 0; padding: 0; box-sizing: border-box; }
  html, body { width: 1200px; height: 1200px; overflow: hidden; }
  body { position: relative; background: var(--white); font-family: "Abel", sans-serif; }

  .topbar { position: absolute; left: 0; top: 0; width: 1200px; height: 35px; background: var(--red); }
  .topbar-inner { position: absolute; right: 110px; top: 0; height: 35px; display: flex; align-items: center; gap: 14px; color: var(--white); font-family: "Roboto Condensed", sans-serif; font-weight: 300; font-size: 17px; letter-spacing: -0.3px; }
  .social { display: flex; gap: 12px; }
  .social span { width: 19px; height: 19px; border-radius: 50%; background: var(--white); display: block; }
  .divider { width: 1px; height: 14px; background: var(--white); margin: 0 6px; }
  .login { display: flex; align-items: center; gap: 10px; }

  .brand { position: absolute; left: 110px; top: 66px; display: flex; align-items: center; gap: 12px; }
  .brand-dot { width: 22px; height: 22px; border-radius: 50%; background: var(--orange); }
  .brand-name { font-family: "Jost", sans-serif; font-weight: 700; color: var(--navy); font-size: 25px; line-height: 28px; text-transform: uppercase; }

  .contact { position: absolute; right: 110px; top: 78px; text-align: right; color: var(--red); }
  .contact .phone { font-family: "Roboto Condensed", sans-serif; font-weight: 400; font-size: 23px; line-height: 30px; letter-spacing: -0.3px; }
  .contact .email { font-family: "Open Sans", sans-serif; font-size: 15px; margin-top: 6px; }

  .nav { position: absolute; left: 110px; top: 166px; width: 980px; border-top: 1px solid var(--rule); height: 40px; }
  .nav ul { list-style: none; display: flex; justify-content: center; gap: 54px; margin-top: 7px; padding-right: 6px; }
  .nav li { font-family: "Open Sans", sans-serif; font-weight: 600; font-size: 17px; color: var(--red); position: relative; }
  .nav li.current::before { content: ""; position: absolute; left: 50%; top: -8px; margin-left: -5px; border-left: 5px solid transparent; border-right: 5px solid transparent; border-top: 5px solid var(--red); }

  .hero { position: absolute; left: 0; top: 206px; width: 1200px; height: 424px;
    background: linear-gradient(180deg, var(--hero-top) 0%, var(--hero-bottom) 100%); }

  .content { position: absolute; left: 0; top: 630px; width: 1200px; height: 492px; background: var(--paper); }
  .welcome { position: absolute; top: 31px; width: 1200px; text-align: center; color: var(--red); font-weight: 400; font-size: 31px; letter-spacing: 1.4px; }
  .intro { position: absolute; left: 110px; top: 93px; width: 980px; text-align: center; color: var(--ink); font-size: 16.5px; line-height: 21px; letter-spacing: 0.45px; }

  .services { position: absolute; left: 111px; top: 267px; display: flex; gap: 26px; }
  .card { position: relative; width: 309px; height: 165px; background: var(--panel); overflow: hidden; }
  .card-band { position: absolute; inset: 0; background: var(--orange); clip-path: polygon(49px 165px, 212px 0, 309px 0, 309px 95px, 236px 165px); }
  .card-title { position: absolute; left: 0; top: 51px; width: 309px; text-align: center; font-family: "Jost", sans-serif; font-weight: 600; font-size: 24px; line-height: 32px; color: var(--white); text-transform: uppercase; }
  .card-arrow { position: absolute; left: 280px; top: 135px; }

  .footer { position: absolute; left: 0; top: 1122px; width: 1200px; height: 78px; background: var(--dark); color: var(--white); }
  .footer-nav { list-style: none; display: flex; justify-content: center; margin-top: 12px; font-size: 13.5px; letter-spacing: 0.3px; }
  .footer-nav li { padding: 0 19px; border-left: 1px solid var(--white); line-height: 15px; }
  .footer-nav li:first-child { border-left: 0; }
  .copyright { text-align: center; font-size: 12.5px; margin-top: 22px; }
</style>
</head>
<body>
  <header>
    <div class="topbar">
      <div class="topbar-inner">
        <div class="social"><span></span><span></span><span></span></div>
        <i class="divider"></i>
        <div class="login">
          <svg width="18" height="18" viewBox="0 0 18 18"><circle cx="6" cy="6" r="4.5" fill="#fff"/><circle cx="6" cy="6" r="1.6" fill="#f23535"/><path d="M8.5 8.5 L16 16 M12.5 12.5 L14.5 10.5 M14.3 14.3 L16 12.6" stroke="#fff" stroke-width="2.4" stroke-linecap="round"/></svg>
          <span>LOGIN</span>
        </div>
        <i class="divider"></i>
        <span>FREE TRIAL</span>
      </div>
    </div>

    <div class="brand">
      <div class="brand-dot"></div>
      <div class="brand-name">Kestrel Sports<br>Management</div>
    </div>

    <div class="contact">
      <div class="phone">+61 400 218 376</div>
      <div class="email">hello@kestrelsports.example</div>
    </div>

    <nav class="nav">
      <ul>
        <li class="current">Home</li>
        <li>About Us</li>
        <li>Services</li>
        <li>Contact Us</li>
      </ul>
    </nav>
  </header>

  <div class="hero" role="img" aria-label="Hero photograph of a football on a stadium pitch"></div>

  <main class="content">
    <h1 class="welcome">WELCOME TO KESTREL SPORTS MANAGEMENT!</h1>
    <p class="intro">Lorem ipsum dolor sit amet conse ctetur adipisicing elit, sed do eiusmod Tempor incididunt ut labore et dolore magna aliqua. Ut enim ad minim veniam, quis Nostrud exercitation ullamco laboris nisi ut aliquip ex ea commodo consequat.<br>Duis aute irure Dolor in reprehenderit in voluptate velit esse cillum dolore eu fugiat nulla pariatur.<br>Excepteur sint occaecat cupidatat non proident, sunt in culpa qui officia Deserunt mollit anim id est laborum. Ut enim ad minim veniam, quis nostrud Exercitation ullamco laboris nisi ut aliquip ex ea commodo consequat.</p>

    <section class="services">
      <div class="card">
        <div class="card-band"></div>
        <div class="card-title">Team<br>Development</div>
        <svg class="card-arrow" width="18" height="20" viewBox="0 0 18 20"><path d="M3 2 L13 10 L3 18" fill="none" stroke="#fff" stroke-width="4"/></svg>
      </div>
      <div class="card">
        <div class="card-band"></div>
        <div class="card-title">Personal<br>Brand Strategy</div>
        <svg class="card-arrow" width="18" height="20" viewBox="0 0 18 20"><path d="M3 2 L13 10 L3 18" fill="none" stroke="#fff" stroke-width="4"/></svg>
      </div>
      <div class="card">
        <div class="card-band"></div>
        <div class="card-title">Education<br>&amp; Training</div>
        <svg class="card-arrow" width="18" height="20" viewBox="0 0 18 20"><path d="M3 2 L13 10 L3 18" fill="none" stroke="#fff" stroke-width="4"/></svg>
      </div>
    </section>
  </main>

  <footer class="footer">
    <ul class="footer-nav">
      <li>Home</li>
      <li>About Us</li>
      <li>Services</li>
      <li>Contact Us</li>
    </ul>
    <p class="copyright">© 2014 Kestrel Sports Management. All Rights reserved | Privacy | Terms of Use</p>
  </footer>
</body>
</html>
```